DOVR Business Card Design Project

Company Name: DOVR (Dove Operational Versatile Resources) JLT.
Office Address: Office No 218, Saffron Crest Tower, Palmera Bay Towers, Dubai, U.A.E
Company line of business:
1) Currently we have a POS solution for retail outlets like duty free shops, supermarkets, department stores etc... The solution is deployed in Harbor Gate Retail on 350 POS and in Coralline Port Retail on 100 POS. So our main line of business is the deployment of this solution in retail outlets locally or regionally. We have already deployed the solution in India and Australia.
2) Integration of other third party POS systems with an online credit authorization netwotk in the UAE. This will enable POS applications to connect directly to the acquiring banks without needing an EFT terminal like Paxoline or Tramodex. The credit card payment is completed at the POS.
3) Other solutions that are targeting retail outlets like mobile POS, queue busting solutions, stock taking solutions using hand held devices, transaction capture systems, etc...
4) Other IT services like support of call center solutions from Bramwell Systems and development of new solutions as per customer requirements.
We need a business card design for the company. We don't have any specific requirements and will eave up to the designers to come up with creative designs. At the moment we still don't have a letter head design and the only thing that we have is the company logo that we will upload shortly.
Updates
Dear All,
I just uploaded the logo source files. I am sorry for the delay.
Regards
Tarek Demirci
I would like the business cards to have the following details:
Company Tel No
Company Fax No
Company Website Address
Employee Name
Employee Title
Employee Mobile Number
Employee Email Address

```html
<!DOCTYPE html>
<html lang="en">
<head>
<meta charset="utf-8">
<title>DOVR Business Card</title>
<link href="https://fonts.googleapis.com/css2?family=Arimo:wght@400;700&display=swap" rel="stylesheet">
<style>
  :root {
    --card-white: #ffffff;
    --card-mist: #e9e9eb;
    --ink: #2b2b2b;
    --brand-blue: #1b6fb3;
    --brand-blue-deep: #0f5596;
    --brand-blue-light: #3d95d6;
    --on-blue: #ffffff;
  }
  html, body {
    margin: 0;
    padding: 0;
    overflow: hidden;
    background: #ffffff;
  }
  .card {
    position: relative;
    width: 1200px;
    height: 705px;
    overflow: hidden;
    font-family: "Arimo", Arial, sans-serif;
    color: var(--ink);
    background: radial-gradient(ellipse 75% 70% at 50% 38%, var(--card-white) 0%, var(--card-white) 45%, var(--card-mist) 100%);
  }
  .wave {
    position: absolute;
    inset: 0;
    width: 1200px;
    height: 705px;
  }
  .brand {
    position: absolute;
    left: 40px;
    top: 48px;
    display: flex;
    align-items: center;
    gap: 26px;
  }
  .brand-dot {
    width: 104px;
    height: 104px;
    border-radius: 50%;
    background: var(--brand-blue);
  }
  .brand-name {
    font-size: 112px;
    font-weight: 700;
    letter-spacing: 2px;
    line-height: 1;
    color: var(--ink);
  }
  .company-line {
    position: absolute;
    left: 38px;
    top: 248px;
    margin: 0;
    font-size: 26px;
    font-weight: 400;
    color: var(--ink);
  }
  .company-contact {
    position: absolute;
    right: 31px;
    top: 32px;
    margin: 0;
    text-align: right;
    font-style: normal;
    font-size: 27px;
    line-height: 40px;
    color: var(--ink);
  }
  .company-contact .address {
    margin-top: 12px;
    line-height: 38px;
  }
  .employee {
    position: absolute;
    left: 31px;
    top: 528px;
    margin: 0;
    font-style: normal;
    font-size: 27px;
    line-height: 36px;
    color: var(--on-blue);
  }
</style>
</head>
<body>
<main class="card">
  <svg class="wave" viewBox="0 0 1200 705" aria-hidden="true">
    <defs>
      <linearGradient id="waveFill" x1="0" y1="0" x2="1" y2="1">
        <stop offset="0" stop-color="var(--brand-blue-light)"/>
        <stop offset="0.45" stop-color="var(--brand-blue)"/>
        <stop offset="1" stop-color="var(--brand-blue-deep)"/>
      </linearGradient>
    </defs>
    <path d="M0,338 C 320,520 720,650 1200,712 L1200,705 L0,705 Z" fill="#ffffff" opacity="0.9"/>
    <path d="M0,356 C 300,535 700,655 1200,718 L1200,705 L0,705 Z" fill="url(#waveFill)"/>
  </svg>

  <div class="brand">
    <span class="brand-dot"></span>
    <span class="brand-name">DOVR</span>
  </div>

  <p class="company-line">DOVR (Dove Operational Versatile Resources) JLT.</p>

  <address class="company-contact">
    <div>Telephone : 555 210 4870</div>
    <div>Fax : 555 210 4870</div>
    <div>Website : info@dovrtech.ae</div>
    <div class="address">
      Address&nbsp; : Office No 218,<br>
      Saffron Crest Tower,<br>
      Palmera Bay Towers,<br>
      Dubai, U.A.E
    </div>
  </address>

  <address class="employee">
    <div>Employee Name</div>
    <div>Employee Title</div>
    <div>Phone : 555 210 4871</div>
    <div>E-mail : info@dovrtech.ae</div>
  </address>
</main>
</body>
</html>
```